T.R.L (Tidal Resonance Lifting) is a form of energy healing that raises the vibration of the DNA so that it releases old energy patterns that no longer serve you. This allows the body to remember its natural ability to heal itself perfectly.

The energy is called in telepathically from the Acturians, the dolphins, the platinum ray and the Octahedron.

I would like a logo that incorporates all of these moadlities.

I will also require help with setting up my facebook page and website but until these are setup I cannot include the details so space will need to be saved for this on the business card

Target Market(s)

Alternative health

Industry/Entity Type

Business

Logo Text

T.R.L

Requirements
Must have
• Colors of the platinum ray. I have drafted the below as to what I would like it to say on it:-

Business Card –
Front:-
Taking you to a higher vibration
Mabel Thornby
Tidal Resonance Lifting Facilitator
www.quorvintel.example
+(61) 412 735 289 mabelthornby4471@quorvintel.example

Back:-
Appointments
For:-
Date: Time:
Location:

```html
<!DOCTYPE html>
<html lang="en">
<head>
<meta charset="utf-8">
<title>Lumen Tide Healing – Business Card</title>
<link rel="stylesheet" href="https://fonts.googleapis.com/css2?family=Arimo:wght@400;700&display=swap">
<style>
  :root {
    --backdrop: #e6e6e6;
    --card-white: #ffffff;
    --brand-blue: #2e88d0;
    --brand-blue-light: #7cc6ec;
    --rule-blue: #8fc0e6;
    --tagline-blue: #1d5f96;
    --soft-blue: #a9d9f5;
    --text-white: #ffffff;
  }
  * { box-sizing: border-box; margin: 0; padding: 0; }
  html, body {
    width: 1200px;
    height: 900px;
    overflow: hidden;
  }
  body {
    position: relative;
    background: var(--backdrop);
    font-family: "Arimo", Arial, sans-serif;
  }

  .card {
    position: absolute;
    top: 116px;
    width: 385px;
    height: 269px;
  }

  /* Appointment side */
  .card--appointments {
    left: 168px;
    background: var(--card-white);
    padding: 52px 80px 0 80px;
  }
  .appointments__title {
    color: var(--brand-blue);
    font-weight: 700;
    font-size: 31px;
    letter-spacing: -0.2px;
    margin-bottom: 34px;
  }
  .appointments__row {
    display: flex;
    gap: 10px;
    margin-bottom: 26px;
  }
  .appointments__field {
    flex: 1;
    color: var(--brand-blue);
    font-size: 10px;
    border-bottom: 1px solid var(--rule-blue);
    padding-bottom: 2px;
  }

  /* Contact side */
  .card--contact {
    left: 648px;
    background:
      radial-gradient(ellipse 220px 90px at 40px 20px, var(--brand-blue-light), transparent 100%),
      var(--brand-blue);
    color: var(--text-white);
    text-align: center;
    padding-top: 44px;
  }
  .contact__name {
    font-weight: 700;
    font-size: 31px;
    letter-spacing: 0.2px;
  }
  .contact__role {
    color: var(--tagline-blue);
    font-size: 11px;
    margin-top: 4px;
  }
  .contact__divider {
    display: block;
    width: 36px;
    height: 6px;
    margin: 12px auto;
    background: var(--soft-blue);
    border-radius: 3px;
    opacity: 0.8;
  }
  .contact__details {
    font-size: 11px;
    line-height: 15px;
  }
  .contact__brand {
    color: var(--soft-blue);
    font-size: 19px;
    margin-top: 4px;
  }

  /* Wordmark */
  .wordmark {
    position: absolute;
    top: 460px;
    left: 0;
    width: 1200px;
    text-align: center;
    color: var(--brand-blue);
    font-size: 64px;
    font-weight: 400;
  }
</style>
</head>
<body>

  <section class="card card--appointments" aria-label="Appointment card">
    <h2 class="appointments__title">Appointments</h2>
    <div class="appointments__row">
      <div class="appointments__field">For:</div>
    </div>
    <div class="appointments__row">
      <div class="appointments__field">Date:</div>
      <div class="appointments__field">Time:</div>
    </div>
    <div class="appointments__row">
      <div class="appointments__field">Location:</div>
    </div>
  </section>

  <section class="card card--contact" aria-label="Contact card">
    <h1 class="contact__name">Mabel Thornby</h1>
    <p class="contact__role">Tidal Resonance Lifting Facilitator</p>
    <span class="contact__divider" role="img" aria-label="small diamond ornament"></span>
    <p class="contact__details">+(61) 412 735 289<br>mabelthornby4471@quorvintel.example</p>
    <span class="contact__divider" role="img" aria-label="small diamond ornament"></span>
    <p class="contact__brand">Lumen Tide Healing</p>
  </section>

  <p class="wordmark">Lumen Tide Healing</p>

</body>
</html>
```